Kids Bamboo sun protection clothing

We need a flyer to promote our bamboo sun protection range to parents of kids with sensitive due to illness or skin conditions.
Our clothing is made from bamboo that has been specially knitted for high sun protection but does not use chemicals. The clothing is for everyday wear, to the playground, going for walks, after a swim. Special features such as hoods, high necklines, long sleeves and thumb loops create more coverage but it is not a lycra rash vest. You can see the product at www.lumora-wear.com. We would like this flyer (or postcard) to show parents with children who are sensitive tot he sun that there is an option. Their kids might have albinism, Cancer or severe burns, might be sensitive to the sun or have Eczema. These clothes are natural fabric with styling to help look after their skin in the sun. We would like a soft caring approach.

Target Market(s)

Mums of children who have sensitive skin due to burns, cancer, Eczema or UV sensitivity.

Industry/Entity Type

Health

Font styles to use
Sans Serif

Requirements
Must have
• Point out how it can protect the skin with fabric and design features.
• Be eye catching so if it is in a waiting room at the doctors people will go over to pick it up. Be a soft approach that does not concentrate on the illness.
• Website details
Nice to have
• mention that we also do women's wear
• Please use any images off the website

```html
<!DOCTYPE html>
<html lang="en">
<head>
<meta charset="utf-8">
<title>Lumora Kids Clothing Flyer</title>
<link rel="stylesheet" href="https://fonts.googleapis.com/css2?family=Fjalla+One&family=Fredoka:wght@600&family=Lato:ital,wght@0,300;0,400;0,700;1,400;1,700&display=swap">
<style>
  :root {
    --orange: #fba933;
    --grey: #666769;
    --ink: #222222;
    --sky: #86aee6;
    --sky-light: #a9c6ef;
    --sand: #e8cfa9;
    --navy: #1f2a4a;
    --white: #ffffff;
    --backdrop: #ececec;
  }
  * { margin: 0; padding: 0; box-sizing: border-box; }
  html, body { width: 1200px; height: 1200px; overflow: hidden; }
  body { background: var(--backdrop); position: relative; font-family: "Lato", sans-serif; color: var(--ink); }

  .flyer {
    position: absolute; left: 185px; top: 20px;
    width: 790px; height: 1105px;
    background: var(--white);
    overflow: hidden;
    transform: scale(1.0498); transform-origin: 0 0;
  }
  .flyer-art { position: absolute; inset: 0; width: 790px; height: 1105px; }

  .brand { position: absolute; left: 53px; top: 45px; width: 227px; }
  .brand-rule { height: 3px; background: var(--orange); }
  .brand-name {
    font-family: "Lato", sans-serif; font-weight: 300; font-size: 52px;
    letter-spacing: 1px; color: var(--grey); line-height: 1; margin-top: 4px;
  }

  .features { position: absolute; left: 52px; top: 556px; width: 230px; }
  .features-title { font-family: "Fredoka", sans-serif; font-weight: 600; font-size: 19px; color: var(--orange); letter-spacing: 1px; }
  .feature-list { list-style: none; margin-top: 17px; }
  .feature-list li {
    position: relative; padding-left: 16px; margin-bottom: 7px; width: 175px;
    font-style: italic; font-weight: 700; font-size: 18.5px; line-height: 21px; color: var(--ink);
  }
  .feature-list li::before {
    content: ""; position: absolute; left: 1px; top: 9px; width: 6px; height: 6px;
    border-radius: 50%; background: var(--orange);
  }
  .mum-note { position: absolute; left: 51px; top: 749px; width: 175px; font-size: 19px; line-height: 24px; }
  .protection-note { position: absolute; left: 51px; top: 809px; width: 205px; font-style: italic; font-size: 18px; line-height: 24px; }
  .contact { position: absolute; left: 45px; width: 260px; display: flex; align-items: flex-start; gap: 6px; }
  .contact-phone { top: 959px; color: var(--orange); font-weight: 700; font-size: 20px; }
  .contact-address { top: 996px; font-size: 17.5px; line-height: 22px; }
  .contact svg { flex: none; margin-top: 3px; }

  .divider { position: absolute; left: 289px; top: 562px; width: 1px; height: 420px; background: #d6d6d6; }

  .headline { position: absolute; left: 317px; top: 548px; font-family: "Fjalla One", sans-serif; line-height: 1; }
  .headline-main { display: block; font-size: 70px; color: var(--grey); }
  .headline-sub { display: block; font-size: 74px; color: var(--orange); margin-top: -4px; letter-spacing: 1px; }

  .intro { position: absolute; left: 319px; top: 704px; width: 345px; font-size: 11px; line-height: 15.2px; color: var(--ink); }
  .tagline { position: absolute; left: 321px; top: 829px; width: 310px; font-weight: 700; font-size: 17px; line-height: 22px; }
  .tagline-link { color: var(--orange); display: block; }
  .cta { position: absolute; left: 321px; top: 915px; font-size: 16.5px; line-height: 22px; }
  .cta-label { color: var(--orange); font-weight: 700; display: block; }
</style>
</head>
<body>
  <div class="flyer">
    <svg class="flyer-art" viewBox="0 0 790 1105" xmlns="http://www.w3.org/2000/svg">
      <defs>
        <linearGradient id="sceneGradient" x1="0" y1="0" x2="0" y2="1">
          <stop offset="0" stop-color="var(--sky)"/>
          <stop offset="0.78" stop-color="var(--sky-light)"/>
          <stop offset="0.86" stop-color="var(--sand)"/>
          <stop offset="1" stop-color="var(--sand)"/>
        </linearGradient>
        <linearGradient id="circleGradient" x1="0" y1="0" x2="0" y2="1">
          <stop offset="0" stop-color="var(--sky)"/>
          <stop offset="0.6" stop-color="var(--sky-light)"/>
          <stop offset="0.72" stop-color="var(--sand)"/>
          <stop offset="1" stop-color="var(--sand)"/>
        </linearGradient>
        <linearGradient id="modelGradient" x1="0" y1="0" x2="0" y2="1">
          <stop offset="0" stop-color="#2b3760"/>
          <stop offset="1" stop-color="var(--navy)"/>
        </linearGradient>
      </defs>

      <g role="img" aria-label="Photo of three children in pastel sun-protective clothing standing on sand holding balloons against a blue wall">
        <rect x="0" y="0" width="790" height="500" fill="url(#sceneGradient)"/>
      </g>

      <path d="M0,0 H400 C380,100 250,185 0,205 Z" fill="var(--white)"/>
      <path d="M0,205 C250,185 380,100 400,0" fill="none" stroke="var(--grey)" stroke-width="9"/>
      <path d="M0,217 C270,196 410,110 437,0" fill="none" stroke="var(--orange)" stroke-width="11"/>

      <path d="M0,283 L48,305 L48,322 L0,300 Z" fill="var(--grey)"/>
      <path d="M0,325 L40,345" stroke="var(--orange)" stroke-width="5"/>

      <path d="M0,470 H300 C430,482 600,470 790,470 V1105 H0 Z" fill="var(--white)"/>
      <path d="M340,482 C480,462 650,455 790,455 V490 C640,486 500,488 360,500 Z" fill="var(--grey)"/>
      <path d="M335,500 C500,512 650,520 790,522 V545 C640,540 480,525 335,500 Z" fill="var(--orange)"/>

      <circle cx="212" cy="380" r="174" fill="var(--white)"/>
      <g role="img" aria-label="Photo of three children playing in the sand wearing hats and long-sleeved sun-protective clothing">
        <circle cx="212" cy="380" r="158" fill="url(#circleGradient)"/>
      </g>
      <circle cx="212" cy="380" r="161" fill="none" stroke="var(--orange)" stroke-width="7"/>

      <path d="M790,540 C760,820 580,1040 270,1105 H380 C620,1050 790,880 790,790 Z" fill="var(--grey)"/>
      <path d="M790,835 C760,965 620,1070 455,1105 H790 Z" fill="var(--orange)"/>

      <g role="img" aria-label="Photo of a boy in a navy hooded vest, striped long-sleeved top and navy track pants">
        <rect x="676" y="690" width="100" height="405" rx="22" fill="url(#modelGradient)"/>
      </g>
    </svg>

    <div class="brand">
      <div class="brand-rule"></div>
      <div class="brand-name">LUMORA</div>
    </div>

    <section class="features">
      <h2 class="features-title">FEATURES</h2>
      <ul class="feature-list">
        <li>High necklines</li>
        <li>Long sleeves</li>
        <li>Thumb loops for hand cover</li>
        <li>Breathable fabrics</li>
      </ul>
    </section>

    <p class="mum-note">WE have things for Mum as well.</p>
    <p class="protection-note">Tested by SUNLAB to UPF 50+ protection, we have your head, arms, legs and hands covered for everyday life outside.</p>

    <div class="contact contact-phone">
      <svg width="15" height="15" viewBox="0 0 24 24" aria-hidden="true"><path d="M6.6 10.8a15.1 15.1 0 0 0 6.6 6.6l2.2-2.2c.3-.3.7-.4 1-.2 1.1.4 2.3.6 3.6.6.6 0 1 .4 1 1V20c0 .6-.4 1-1 1A17 17 0 0 1 3 4c0-.6.4-1 1-1h3.5c.6 0 1 .4 1 1 0 1.3.2 2.5.6 3.6.1.3 0 .7-.2 1z" fill="none" stroke="var(--orange)" stroke-width="2"/></svg>
      <span>03 9555 0142</span>
    </div>
    <div class="contact contact-address">
      <svg width="15" height="19" viewBox="0 0 24 30" aria-hidden="true"><path d="M12 0C5.4 0 0 5.2 0 11.7 0 20 12 30 12 30s12-10 12-18.3C24 5.2 18.6 0 12 0zm0 16.5a4.8 4.8 0 1 1 0-9.6 4.8 4.8 0 0 1 0 9.6z" fill="var(--orange)"/></svg>
      <span>24 Wattle Lane,<br>Fairview Vic 3999</span>
    </div>

    <div class="divider"></div>

    <h1 class="headline">
      <span class="headline-main">Lumora Kids</span>
      <span class="headline-sub">CLOTHING</span>
    </h1>

    <p class="intro">Our children's skin is so soft and delicate Some little ones need extra protection from the sun in a way that cares for their delicate skin If your little one- Has sensitive skin due to medication Has a burn or scar that is not sun friendly Is sensitive to uncomfortable clothes Or Is UV sensitive Then we might be able to help Our Little Lumora range is 100% Australian made bamboo jersey made especially for everyday sun protection.</p>

    <p class="tagline">Life is for living,bring back fresh air and flowers in clothes <span class="tagline-link">from Lumora-wear.com</span></p>

    <p class="cta"><span class="cta-label">See more</span>at www.lumora-wear.com</p>
  </div>
</body>
</html>
```